Digital Menu Board for Restaurant

I want a digital menu board for our new restaurant. I have provided the sample of what I kind of want.
This is to be on a 55 inch tv so it needs to be the correct aspect ratio of 4:5

Font styles to use
Serif
Sans Serif

Colors
f59296
f04a50
ec1f27
ffffff
fffef7
fbed22
ffc214
0592cd
e5519f

Requirements
Must have
• fun, maybe something moving? bright colors on a darker background so it's easy to read or dark font on a light background.

```html
<!DOCTYPE html>
<html lang="en">
<head>
<meta charset="utf-8">
<title>Sandy Cove Menu Board</title>
<link rel="stylesheet" href="https://fonts.googleapis.com/css2?family=Oswald:wght@700&family=Poppins:ital,wght@0,800;1,700;1,800&display=swap">
<style>
  :root {
    --pink: #e5519f;
    --red: #ec1f27;
    --coral: #f04a50;
    --yellow: #fbed22;
    --gold: #ffc214;
    --blue: #0592cd;
    --white: #ffffff;
    --cream: #fffef7;
    --board: #1d1d1d;
    --page: #efefef;
  }
  * { margin: 0; padding: 0; box-sizing: border-box; }
  html, body { width: 897px; height: 1200px; overflow: hidden; }
  body { background: var(--page); position: relative; }

  .menu-board {
    position: absolute; left: 0; top: 348px;
    width: 897px; height: 504px;
    background: var(--board);
    overflow: hidden;
    font-family: "Poppins", sans-serif;
  }
  .column { position: absolute; top: 0; height: 504px; background: var(--board); }
  .col-buns { left: 0; width: 329px; }
  .col-center { left: 331px; width: 230px; }
  .col-shore { left: 563px; width: 334px; }

  .section-head {
    position: absolute; left: 0; top: 0; width: 100%; height: 70px;
    background: var(--pink);
  }
  .section-title {
    position: absolute;
    font-family: "Oswald", sans-serif; font-weight: 700;
    color: #111; font-size: 41px; line-height: 1; letter-spacing: 0.5px;
    top: 16px; left: 22px;
  }
  .col-shore .section-title { left: 17px; }

  .item { position: absolute; left: 26px; white-space: nowrap; }
  .col-shore .item { left: 22px; }
  .item-name {
    color: var(--gold); font-weight: 800; font-style: italic;
    font-size: 19.5px; line-height: 21px;
  }
  .item-desc {
    color: var(--cream); font-weight: 700; font-style: italic;
    font-size: 10.2px; line-height: 13.5px;
  }

  .combo-band {
    position: absolute; left: 0; top: 401px; width: 100%; height: 39px;
    background: var(--red);
  }
  .combo-title {
    position: absolute; left: 26px; top: 2px;
    font-family: "Oswald", sans-serif; font-weight: 700;
    color: var(--white); font-size: 32px; line-height: 1;
  }
  .combo-list {
    position: absolute; left: 26px; top: 443px;
    color: var(--yellow); font-weight: 800; font-style: italic;
    font-size: 16px; line-height: 19px; list-style: none;
  }

  .brand {
    position: absolute; left: 0; top: 30px; width: 100%;
    display: flex; align-items: center; justify-content: center; gap: 7px;
  }
  .brand-dot { width: 14px; height: 14px; border-radius: 50%; background: var(--gold); }
  .brand-name {
    color: var(--coral); font-weight: 800; font-size: 27px; line-height: 1;
  }
  .hero-photo { position: absolute; left: 0; top: 100px; }

  .band { position: absolute; left: 0; width: 100%; }
  .band-kids { top: 236px; height: 33px; background: var(--red); }
  .band-shakes { top: 345px; height: 32px; background: var(--yellow); }
  .band-title {
    position: absolute; top: 2px; width: 100%; text-align: center;
    font-family: "Oswald", sans-serif; font-weight: 700; line-height: 1;
  }
  .band-kids .band-title { color: var(--white); font-size: 24px; }
  .band-kids .band-title small { font-size: 14px; }
  .band-shakes .band-title { color: #111; font-size: 28px; }

  .plain-list {
    position: absolute; left: 11px; list-style: none;
    color: var(--cream); font-weight: 700; font-style: italic;
    font-size: 10.2px; line-height: 12.6px; white-space: nowrap;
  }
  .kids-list { top: 280px; }
  .shakes-list { top: 383px; line-height: 13.4px; }

  .extras-band {
    position: absolute; left: 0; top: 312px; width: 100%; height: 33px;
    background: var(--gold);
  }
  .extras-title {
    position: absolute; top: 1px;
    font-family: "Oswald", sans-serif; font-weight: 700;
    color: #111; font-size: 29px; line-height: 1;
  }
  .title-side { left: 22px; }
  .title-drinks { left: 163px; }
  .extras-divider {
    position: absolute; left: 155px; top: 312px; width: 2px; height: 192px;
    background: var(--white);
  }
  .band-gap { position: absolute; left: 153px; top: 312px; width: 4px; height: 33px; background: var(--board); }

  .side-list {
    position: absolute; left: 22px; top: 360px; list-style: none;
    color: var(--cream); font-weight: 800; font-style: italic;
    font-size: 12.2px; line-height: 17.2px; white-space: nowrap;
  }
  .drink-list {
    position: absolute; top: 360px; list-style: none;
    color: var(--gold); font-weight: 800; font-style: italic;
    font-size: 11.6px; line-height: 15.6px; white-space: nowrap;
  }
  .drinks-a { left: 171px; }
  .drinks-b { left: 254px; }
  .corner-art {
    position: absolute; left: 218px; top: 440px; width: 92px; height: 50px;
  }
</style>
</head>
<body>
  <main class="menu-board">

    <section class="column col-buns">
      <header class="section-head"><h2 class="section-title">BETWEEN BUNS</h2></header>

      <div class="item" style="top:76px">
        <div class="item-name">1st Point Pulled Pork</div>
        <div class="item-desc">Pulled Pork, Mack's Sassy BBQ Sauce,<br>Chopped Bacon, Pepperjack Cheese, and Fried<br>Jalapeno Pepers on Ciabatta Bun</div>
      </div>
      <div class="item" style="top:143px">
        <div class="item-name">2nd Point Pulled Pork</div>
        <div class="item-desc">Pulled Pork, Mack's Sweet Raspberry BBQ<br>Sauce, and Coleslaw on a Ciabatta Bun</div>
      </div>
      <div class="item" style="top:199px">
        <div class="item-name">Spiniker Point Burger</div>
        <div class="item-desc">Smokehouse 1/2 Pound Burger, Crumbled<br>Bacon, Mack's Sassy BBQ Sauce, Cheese, and<br>Onion Rings on a Toasted Brioche Bun</div>
      </div>
      <div class="item" style="top:267px">
        <div class="item-name">The Rock Burger</div>
        <div class="item-desc">Two Smokehouse 1/2 Pound Patties, Cheese,<br>Lettuce, Tomato, Onion, Pickles, on toasted<br>Brioche Bun</div>
      </div>
      <div class="item" style="top:334px">
        <div class="item-name">Rainbow Cove Sandwich</div>
        <div class="item-desc">Chicken Salad - Smoked Chicken Celery, and<br>Onion Mixed with our BBQ Mayo and Topped<br>with Sea-soned Tomato on a Hoagie Roll.</div>
      </div>

      <div class="combo-band"><h3 class="combo-title">COMBO UP!</h3></div>
      <ul class="combo-list">
        <li>Add 1 Side and Drink</li>
        <li>Add 1 Side and Shake</li>
        <li>Additional Sides</li>
      </ul>
    </section>

    <section class="column col-center">
      <div class="brand">
        <span class="brand-dot"></span>
        <span class="brand-name">Sandy Cove</span>
      </div>

      <svg class="hero-photo" width="230" height="136" viewBox="0 0 230 136" role="img" aria-label="Photo of a pulled pork sandwich on a hoagie roll with BBQ drizzle and sprouts">
        <defs>
          <linearGradient id="photoTone" x1="0" y1="0" x2="1" y2="1">
            <stop offset="0" stop-color="#3f8fb3"/>
            <stop offset="0.5" stop-color="#b98a5c"/>
            <stop offset="1" stop-color="#4a3a30"/>
          </linearGradient>
        </defs>
        <polygon points="0,2 115,49 230,2 230,136 0,136" fill="url(#photoTone)"/>
      </svg>

      <div class="band band-kids"><h3 class="band-title">SEASHELL FINDERS <small>(KIDS)</small></h3></div>
      <ul class="plain-list kids-list">
        <li>Little Cheeseburger</li>
        <li>Pulled pork sandwich</li>
        <li>Mini Corn Dogs</li>
        <li>Chicken salad sandwich</li>
        <li>Fries/Onion Rings</li>
      </ul>

      <div class="band band-shakes"><h3 class="band-title">SHAKES</h3></div>
      <ul class="plain-list shakes-list">
        <li>Mack's Signature Raspberry<br>Jammin Shake</li>
        <li>Raspberry Cookie Crumble Shake</li>
        <li>Raspberry Hazelnut BombShake</li>
        <li>Raspberry Brownie Shake</li>
        <li>Caramel Shake</li>
        <li>Chocolate Shake</li>
        <li>Raspberry Beachin' Shake (Pina Colada)</li>
      </ul>
    </section>

    <section class="column col-shore">
      <header class="section-head"><h2 class="section-title">GREEN SHORE</h2></header>

      <div class="item" style="top:76px">
        <div class="item-name">North Beach Salad</div>
        <div class="item-desc">Pulled pork and Black Beans on a Bed of<br>Romaine, tomato and Onion with Sweet and<br>Sour Raspberry Pineapple Sauce. West Side<br>Salad</div>
      </div>
      <div class="item" style="top:159px">
        <div class="item-name">West Side Salad</div>
        <div class="item-desc">BBQ Pulled Pork, Crumbled Bacon, Candied<br>Walnuts, Feta Cheese, Red Onion, Spinach and<br>Lettuce with Ranch Dressing or Raspberry<br>Vinaigrette</div>
      </div>
      <div class="item" style="top:243px">
        <div class="item-name">East Side Salad</div>
        <div class="item-desc">Spinach and Lettuce, Chopped Apples,<br>Candied Walnuts, Onion, Feta Cheese with<br>Mack's Raspberry Vinaigrette Add Chicken:</div>
      </div>

      <div class="extras-band">
        <h3 class="extras-title title-side">SIDE</h3>
        <h3 class="extras-title title-drinks">DRINKS</h3>
      </div>
      <div class="band-gap"></div>
      <div class="extras-divider"></div>

      <ul class="side-list">
        <li>Seasoned Fries</li>
        <li>Onion Rings</li>
        <li>Sweet Cornbread</li>
        <li>Sweet Coleslaw</li>
        <li>Macaroni Salad</li>
        <li>Side Salad</li>
      </ul>
      <ul class="drink-list drinks-a">
        <li>Fizz Cola</li>
        <li>Diet Fizz</li>
        <li>Cola Classic</li>
        <li>Diet Classic</li>
        <li>Mountain Zing</li>
      </ul>
      <ul class="drink-list drinks-b">
        <li>Diet Zing</li>
        <li>Lemonade</li>
        <li>Lime Pop</li>
        <li>Dr Spark</li>
      </ul>

      <svg class="corner-art" viewBox="0 0 92 50" role="img" aria-label="Decorative seagulls in flight">
        <rect width="92" height="50" rx="6" fill="var(--blue)" opacity="0.18"/>
      </svg>
    </section>

  </main>
</body>
</html>
```